IT Company WebPage Relaunch looking for modern and clean approach

We are looking to relaunch our website, to give it a more modern and clean look.
Company Background:
With nearly 20 years of industry expertise, we've been committed to delivering top-notch professional services and products, ensuring client success and efficiency. Our mission is to provide clients with talented human and technological resources, employing industry best practices for effective solutions. We envision becoming a pivotal player in Dominican Republic's Techonology sector, expanding our footprint across the Caribbean Central America and USA
Design Objectives:
1. Brand Identity: The website should reflect our brand identity based in our logo, color scheme, and overall aesthetic. Consistency with existing brand materials is essential.
2. User Experience: Prioritize user experience by ensuring easy navigation and intuitive layout. The website should be accessible and responsive across various devices and screen sizes.
3. Content Presentation: Present our content (text, images, videos) in a visually appealing and organized manner. Use creative layouts and typography to enhance readability and engagement.
4. Functionality: Implement necessary features and functionalities to support our business objectives. This may include contact form.
5. SEO Optimization: Design the website with search engine optimization (SEO) best practices in mind to improve visibility and ranking on search engine results pages (SERPs).
6. Multilanguage: Spanish and English
Pages and Sections:
1. Home Page:
o Welcome message/introduction
o Highlights of key products/services
o Clear navigation to other sections/pages
o Metrics (10 Satisfied customer) (Services provided in 5 countries) etc.
2. About Us:
o Company overview
o Mission, vision, and values
o Team/Staff profiles (tentative)
3. Products/Services:
o Our Partners
o Detailed descriptions of products/services offered
o Images/videos
4. Portfolio/Projects:
o Our Customers
o Case Studies
o Customer’s testimonials
5. Blog/News:
o Platform for sharing industry insights, updates, or company news
o Categories/tags for easy browsing
6. Contact Us:
o Contact form
o Company address, phone number, email
o Social media links
Design Preferences:
• Clean and modern design aesthetic
• Use of whitespace to enhance readability and visual appeal
• High-quality images and graphics
• Responsive to multiple devices
Technical Requirements:
• Compatibility with major web browsers (Chrome, Firefox, Safari, Edge)
• Compliance with web standards and best practices
Current Website:
https://www.corvantel.com.do
Note: The website should not be on Wordpress, we want an html/css website.

```html
<!DOCTYPE html>
<html lang="en">
<head>
<meta charset="utf-8">
<title>Corvantel — IT Consulting and Services</title>
<link href="https://fonts.googleapis.com/css2?family=Exo+2:wght@500;600;700&family=Lato:wght@400;700&display=swap" rel="stylesheet">
<style>
:root{
  --orange:#f26a2e;
  --orange-light:#f89a34;
  --red:#e0302a;
  --dark-red:#b81f2a;
  --ink:#1c1c1c;
  --text:#3a3a3a;
  --muted:#8a8a8a;
  --grey-bg:#f2f2f2;
  --card-grey:#6b6b6b;
  --footer:#1b1b1b;
  --white:#fff;
}
*{box-sizing:border-box;margin:0;padding:0}
html,body{width:1200px;height:3727px;overflow:hidden}
body{font-family:"Lato",sans-serif;color:var(--text);background:var(--white);position:relative}
.abs{position:absolute}
h1,h2,h3,.heading{font-family:"Exo 2",sans-serif}
.btn{position:absolute;display:flex;align-items:center;justify-content:center;background:linear-gradient(90deg,var(--orange),var(--orange-light));color:var(--white);font-family:"Exo 2",sans-serif;font-weight:700;font-size:15px;border-radius:6px;box-shadow:0 4px 10px rgba(0,0,0,.18);text-transform:uppercase}
.accent{color:var(--red)}
.section-title{position:absolute;left:0;width:1200px;text-align:center;font-size:42px;font-weight:600;color:var(--ink)}

/* header */
.site-header{position:absolute;left:0;top:0;width:1200px;height:85px;background:var(--white);box-shadow:0 2px 6px rgba(0,0,0,.08);z-index:2}
.brand{position:absolute;left:107px;top:20px;display:flex;align-items:center;gap:10px}
.brand-mark{width:40px;height:40px;border-radius:50%;background:var(--orange)}
.brand-name{font-family:"Exo 2",sans-serif;font-weight:700;font-size:28px;color:var(--ink);line-height:1}
.brand-tag{font-size:10px;color:var(--ink);letter-spacing:.3px;margin-top:3px}
.main-nav{position:absolute;top:33px;left:414px;display:flex;gap:34px;font-size:15px;color:var(--ink)}
.lang{position:absolute;left:1043px;top:33px;font-weight:700;font-size:14px;color:var(--ink);display:flex;gap:8px;align-items:center}

/* hero */
.hero{position:absolute;left:0;top:85px;width:1200px;height:529px;background:linear-gradient(90deg,#f5ebe8 0%,#eddcd3 35%,#b89a86 60%,#7a6a60 100%)}
.hero-kicker{position:absolute;left:111px;top:106px;font-family:"Exo 2",sans-serif;font-weight:700;font-size:20px;color:var(--ink)}
.hero-title{position:absolute;left:109px;top:136px;font-size:62px;font-weight:700;color:var(--ink);letter-spacing:1px}
.hero-text{position:absolute;left:111px;top:218px;width:345px;font-size:14.5px;line-height:29px;color:var(--ink)}

/* about */
.about-emblem{position:absolute;left:130px;top:690px;width:340px;height:340px;border-radius:50%;background:radial-gradient(circle at 40% 40%,#f9b08a,#f26a2e 55%,#e0302a)}
.about-title{position:absolute;left:555px;top:704px;font-size:41px;font-weight:600;color:var(--ink)}
.about-text{position:absolute;left:555px;top:766px;width:535px;font-size:14.5px;line-height:27.5px;color:var(--text)}
.about-text p+p{margin-top:27px}

/* services */
.services{position:absolute;left:0;top:1115px;width:1200px;height:553px;background:var(--grey-bg)}
.service-card{position:absolute;top:131px;width:290px;height:345px;background:var(--white);border-radius:4px;box-shadow:0 2px 10px rgba(0,0,0,.08);border-bottom:8px solid var(--orange)}
.service-card .photo{position:absolute;left:10px;top:12px;width:270px;height:263px;border-radius:3px}
.service-card h3{position:absolute;left:0;width:100%;top:294px;text-align:center;font-size:19px;font-weight:500;color:var(--ink)}
.carousel-arrow{position:absolute;top:1404px;width:30px;height:30px;border-radius:50%;background:#111;display:flex;align-items:center;justify-content:center}

/* stats */
.stats{position:absolute;left:0;top:1668px;width:1200px;height:304px;background:linear-gradient(100deg,#f05a2a 0%,#f26a2e 40%,#f8a036 100%)}
.stat{position:absolute;top:60px;width:300px;text-align:center;color:var(--white);font-family:"Exo 2",sans-serif}
.stat .num{font-size:62px;font-weight:600;line-height:1}
.stat .label{margin-top:22px;font-size:20px;font-weight:500;line-height:41px;text-transform:uppercase}
.divider{position:absolute;top:45px;width:1px;height:210px;background:rgba(255,255,255,.7)}
.divider::after{content:"";position:absolute;left:-6px;top:99px;width:13px;height:13px;border-radius:50%;background:var(--white)}

/* projects */
.project{position:absolute}

/* news */
.news{position:absolute;left:0;top:2773px;width:1200px;height:435px;background:#f6f6f6}
.news-card{position:absolute;top:123px;width:463px;height:252px;background:var(--white);border:2px solid #ececec}
.news-card .photo{position:absolute;left:16px;top:17px;width:193px;height:214px}
.news-card h3{position:absolute;left:240px;top:32px;font-family:"Lato",sans-serif;font-weight:400;font-size:17px;color:var(--ink)}
.news-date{position:absolute;left:240px;top:70px;font-size:12px;color:var(--muted);display:flex;gap:8px;align-items:center}
.news-excerpt{position:absolute;left:240px;top:100px;width:200px;font-size:12.5px;line-height:23px;color:var(--muted)}
.read-more{position:absolute;left:240px;top:200px;font-size:13px;font-weight:700;color:var(--ink);text-decoration:underline}

/* footer */
.site-footer{position:absolute;left:0;top:3208px;width:1200px;height:519px;background:var(--footer);color:var(--white)}
.field{position:absolute;top:53px;width:258px;height:47px;background:var(--white);border-radius:6px;color:var(--ink);font-size:12.5px;padding-left:15px;display:flex;align-items:center}
.rule{position:absolute;left:111px;width:977px;height:1px;background:#555}
.footer-brand{position:absolute;left:111px;top:199px;width:299px;height:98px;background:var(--white);display:flex;align-items:center;justify-content:center;gap:10px}
.footer-col h4{position:absolute;top:200px;font-family:"Exo 2",sans-serif;font-weight:600;font-size:20px;text-transform:uppercase}
.footer-list{position:absolute;top:246px;list-style:none;font-size:15px}
.footer-list li{height:34.5px;display:flex;align-items:center;gap:12px}
.contact-row{position:absolute;left:887px;display:flex;gap:14px;align-items:center;font-size:15px;line-height:27px}
.contact-icon{width:32px;height:32px;border-radius:50%;background:var(--white);display:flex;align-items:center;justify-content:center;flex:none}
.copyright{position:absolute;left:0;top:478px;width:1200px;text-align:center;font-size:15px}
</style>
</head>
<body>

<header class="site-header">
  <div class="brand">
    <div class="brand-mark"></div>
    <div>
      <div class="brand-name">CORVANTEL</div>
      <div class="brand-tag">IT CONSULTING AND SERVICES</div>
    </div>
  </div>
  <nav class="main-nav">
    <span>HOME</span><span>ABOUT US</span><span>SERVICES</span><span>PROJECTS</span><span>NEWS</span>
  </nav>
  <a class="btn" style="left:884px;top:22px;width:132px;height:42px;border-radius:5px">Contact Us</a>
  <div class="lang">EN
    <svg width="20" height="20" viewBox="0 0 20 20" fill="none" stroke="#1c1c1c" stroke-width="1.4"><circle cx="10" cy="10" r="8.5"/><ellipse cx="10" cy="10" rx="3.8" ry="8.5"/><path d="M1.5 10h17M3 5.5h14M3 14.5h14"/></svg>
  </div>
</header>

<section class="hero">
  <div class="abs" role="img" aria-label="Smiling businesswoman at a desk with a laptop, meeting a client" style="left:480px;top:0;width:720px;height:529px;background:linear-gradient(90deg,rgba(0,0,0,0),rgba(60,45,35,.25))"></div>
  <div class="hero-kicker">WELCOME TO</div>
  <h1 class="hero-title">CORVAN <span class="accent">TEL</span></h1>
  <p class="hero-text">Corvantel stands out for providing professional services and technological solutions that optimize its clients' processes, thus driving their growth.</p>
  <a class="btn" style="left:111px;top:322px;width:132px;height:43px">Get Started</a>
</section>

<section class="about">
  <div class="about-emblem" role="img" aria-label="Large brand emblem"></div>
  <h2 class="about-title">ABOUT <span class="accent">CORVANTEL</span></h2>
  <div class="about-text">
    <p>With a history of almost two decades in the market, Corvantel stands out for providing professional services and technological solutions that optimize its clients' processes, thus driving their growth.</p>
    <p>Our team is made up of experts in various areas, such as software development, service management, information security and API administration, guaranteeing a comprehensive and cutting-edge approach to each project.</p>
  </div>
  <a class="btn" style="left:555px;top:979px;width:151px;height:46px">View Our Team</a>
</section>

<section class="services">
  <h2 class="section-title" style="top:44px">SOLUTIONS AND <span class="accent">SERVICES</span></h2>
  <article class="service-card" style="left:111px">
    <div class="photo" role="img" aria-label="Two colleagues reviewing documents and a tablet in an office" style="background:linear-gradient(160deg,#c9c4bd,#4a5468)"></div>
    <h3>Software Factory</h3>
  </article>
  <article class="service-card" style="left:455px;border-bottom-color:var(--dark-red)">
    <div class="photo" role="img" aria-label="Team meeting around a table in a glass-walled office" style="background:linear-gradient(160deg,#9fb6cf,#3d5b7e)"></div>
    <h3>Service Management</h3>
  </article>
  <article class="service-card" style="left:798px;border-bottom-color:var(--card-grey)">
    <div class="photo" role="img" aria-label="Two businessmen discussing over a tablet" style="background:linear-gradient(160deg,#d6d6d6,#4b5260)"></div>
    <h3>Infrastructure</h3>
  </article>
</section>
<div class="carousel-arrow" style="left:43px"><svg width="12" height="12" viewBox="0 0 12 12"><path d="M8 1L3 6l5 5" stroke="#fff" stroke-width="2" fill="none"/></svg></div>
<div class="carousel-arrow" style="left:1123px"><svg width="12" height="12" viewBox="0 0 12 12"><path d="M4 1l5 5-5 5" stroke="#fff" stroke-width="2" fill="none"/></svg></div>

<section class="stats">
  <div class="stat" style="left:58px"><div class="num">20</div><div class="label">Years of industry<br>expertise</div></div>
  <div class="divider" style="left:404px"></div>
  <div class="stat" style="left:451px"><div class="num">10</div><div class="label">Satisfied customer</div></div>
  <div class="divider" style="left:790px"></div>
  <div class="stat" style="left:832px"><div class="num">5</div><div class="label">Services provided in<br>countries</div></div>
</section>

<section class="projects">
  <h2 class="section-title" style="top:2026px">OUR <span class="accent">PROJECTS</span></h2>
  <div class="project" role="img" aria-label="Thoughtful senior consultant reviewing work with a colleague" style="left:111px;top:2116px;width:317px;height:241px;background:linear-gradient(150deg,#dcdad6,#8f8a84)"></div>
  <div class="project" role="img" aria-label="Colleagues collaborating on a laptop at a desk" style="left:437px;top:2116px;width:369px;height:241px;background:linear-gradient(150deg,#e6e2dd,#4e4a48)"></div>
  <div class="project" role="img" aria-label="Team reviewing a tablet in a bright office" style="left:814px;top:2116px;width:274px;height:241px;background:linear-gradient(150deg,#e9e6e1,#b06a3a)"></div>
  <div class="project" role="img" aria-label="Diverse team smiling in a meeting room with a whiteboard" style="left:111px;top:2367px;width:695px;height:240px;background:linear-gradient(120deg,#e6ecef,#a7b2ba 55%,#3c3f46)"></div>
  <div class="project" role="img" aria-label="Group meeting around a conference table" style="left:814px;top:2367px;width:274px;height:240px;background:linear-gradient(150deg,#eeeeec,#6e6459)"></div>
  <a class="btn" style="left:507px;top:2667px;width:186px;height:47px">View Testimonials</a>
</section>

<section class="news">
  <h2 class="section-title" style="top:40px">LATEST <span class="accent">NEWS</span></h2>
  <article class="news-card" style="left:110px">
    <div class="photo" role="img" aria-label="Colleagues reviewing charts at a desk" style="background:linear-gradient(150deg,#c8ccd0,#3d4450)"></div>
    <h3>Temporibus autem quibus</h3>
    <div class="news-date"><svg width="14" height="14" viewBox="0 0 14 14" fill="none" stroke="#8a8a8a"><rect x="1" y="2.5" width="12" height="10.5" rx="1"/><path d="M1 6h12M4 1v3M10 1v3"/></svg>13 April 2024</div>
    <p class="news-excerpt">Temporibus autem quibusdam et aut officiis debitis aut rerum ut et voluptates andae sint et molestiae non recusandae.</p>
    <span class="read-more">Read More</span>
  </article>
  <article class="news-card" style="left:622px">
    <div class="photo" role="img" aria-label="Two businessmen talking at a meeting table" style="background:linear-gradient(150deg,#d7d9da,#4a4f57)"></div>
    <h3>Itaque earum rerum</h3>
    <div class="news-date"><svg width="14" height="14" viewBox="0 0 14 14" fill="none" stroke="#8a8a8a"><rect x="1" y="2.5" width="12" height="10.5" rx="1"/><path d="M1 6h12M4 1v3M10 1v3"/></svg>22 April 2024</div>
    <p class="news-excerpt">Itaque earum rerum hic tenetur a sapiente delectus, ut aut reiciendis voluptatatur aut perferendis doloribus</p>
    <span class="read-more">Read More</span>
  </article>
</section>

<footer class="site-footer">
  <div class="field" style="left:111px">Name</div>
  <div class="field" style="left:387px">Email</div>
  <div class="field" style="left:663px">Phone Number</div>
  <a class="btn" style="left:937px;top:53px;width:151px;height:47px">Submit</a>
  <div class="rule" style="top:152px"></div>

  <div class="footer-brand">
    <div class="brand-mark"></div>
    <div>
      <div class="brand-name" style="font-size:30px">CORVANTEL</div>
      <div class="brand-tag" style="font-size:11px">IT CONSULTING AND SERVICES</div>
    </div>
  </div>

  <div class="footer-col">
    <h4 style="left:488px">Quick Links</h4>
    <ul class="footer-list" style="left:488px">
      <li><svg width="13" height="12" viewBox="0 0 13 12" fill="#fff"><path d="M0 5h8V1l5 5-5 5V7H0z"/></svg>Home</li>
      <li><svg width="13" height="12" viewBox="0 0 13 12" fill="#fff"><path d="M0 5h8V1l5 5-5 5V7H0z"/></svg>About</li>
      <li><svg width="13" height="12" viewBox="0 0 13 12" fill="#fff"><path d="M0 5h8V1l5 5-5 5V7H0z"/></svg>Services</li>
      <li><svg width="13" height="12" viewBox="0 0 13 12" fill="#fff"><path d="M0 5h8V1l5 5-5 5V7H0z"/></svg>Projects</li>
      <li><svg width="13" height="12" viewBox="0 0 13 12" fill="#fff"><path d="M0 5h8V1l5 5-5 5V7H0z"/></svg>Contact Us</li>
    </ul>
    <h4 style="left:696px">Help Links</h4>
    <ul class="footer-list" style="left:696px">
      <li><svg width="13" height="12" viewBox="0 0 13 12" fill="#fff"><path d="M0 5h8V1l5 5-5 5V7H0z"/></svg>FAQ</li>
      <li><svg width="13" height="12" viewBox="0 0 13 12" fill="#fff"><path d="M0 5h8V1l5 5-5 5V7H0z"/></svg>Terms of use</li>
      <li><svg width="13" height="12" viewBox="0 0 13 12" fill="#fff"><path d="M0 5h8V1l5 5-5 5V7H0z"/></svg>Privacy Policy</li>
      <li><svg width="13" height="12" viewBox="0 0 13 12" fill="#fff"><path d="M0 5h8V1l5 5-5 5V7H0z"/></svg>Support Links</li>
      <li><svg width="13" height="12" viewBox="0 0 13 12" fill="#fff"><path d="M0 5h8V1l5 5-5 5V7H0z"/></svg>Conditions</li>
    </ul>
    <h4 style="left:887px">Contact Us</h4>
  </div>
  <div class="contact-row" style="top:245px">
    <span class="contact-icon"><svg width="14" height="18" viewBox="0 0 14 18"><path d="M7 0a7 7 0 0 0-7 7c0 5 7 11 7 11s7-6 7-11a7 7 0 0 0-7-7zm0 10a3 3 0 1 1 0-6 3 3 0 0 1 0 6z" fill="#1b1b1b"/></svg></span>
    <span>Corvantel<br>United States</span>
  </div>
  <div class="contact-row" style="top:314px">
    <span class="contact-icon"><svg width="16" height="16" viewBox="0 0 16 16"><path d="M3.5 1l2.5 3-1.5 2a9 9 0 0 0 5 5l2-1.5 3 2.5-1.5 2.5C8 15 1 8 1 2.5z" fill="#1b1b1b"/></svg></span>
    <span>809-555-0184</span>
  </div>
  <div class="contact-row" style="top:365px">
    <span class="contact-icon"><svg width="16" height="12" viewBox="0 0 16 12"><rect width="16" height="12" rx="1.5" fill="#1b1b1b"/><path d="M1 1.5l7 5 7-5" stroke="#fff" stroke-width="1.3" fill="none"/></svg></span>
    <span>info@corvantel.com.do</span>
  </div>

  <div class="rule" style="top:443px"></div>
  <p class="copyright">Copyrights@2024.Corvantel.All Rights Reserved</p>
</footer>

</body>
</html>
```